Morning Harbor Community Chapel needs a new Business Card/Letterhead Suite

***** IT DOES NOT HAVE TO FEATURE GREEN AND BROWN in order to be a successful design*****

****FONTS: SF New Republic, 'Morning Harbor'; Nexa Light, 'Community Chapel'****

***We have two locations, with two addresses. So the business card AND letterhead need to include two sets of address information***

We are a growing church in New York in need of a new stationary suite. We have recently adopted a new logo (via a successful PixelGuild project) and need new business cards, letterhead, envelopes, and folders.

We would like to see creative, original designs that are modern and clean/elegant (NOT dated "churchy" graphics that are cheesy).

We need this project worked on immediately, as we need to print new business cards for upcoming programs we have on our schedule. So, the designs need to be solid so that we can move quickly throughout the revision process toward print.

We'd also need editables files, so that we can drop in other staff members names/phone numbers, to be able to print cards for those staff needing them.

Requirements
Must have
• Our logo
• Must be given to us in an editable format (to change names)
Nice to have
• Some examples on grey, or recycled, card stock
• card stock (background) does not have to be white
Should not have
• Any extraneous logo's or symbols

```html
<!DOCTYPE html>
<html lang="en">
<head>
<meta charset="utf-8">
<title>Morning Harbor Community Chapel — Stationery Suite</title>
<link rel="stylesheet" href="https://fonts.googleapis.com/css2?family=Questrial&family=Josefin+Sans:wght@300&display=swap">
<style>
  :root {
    --brand-green: #3e7b3b;
    --olive-dark: #655f38;
    --olive-board: #958f5f;
    --lime: #cfe07b;
    --paper: #ffffff;
    --sky: #c3e5e7;
  }
  html, body {
    margin: 0;
    padding: 0;
    width: 1200px;
    height: 1200px;
    overflow: hidden;
    background: var(--olive-board);
  }
  .board {
    position: relative;
    width: 1181px;
    height: 1181px;
    transform: scale(1.01609);
    transform-origin: 0 0;
  }
  .board__sky {
    position: absolute;
    left: 0; top: 0;
    width: 1181px; height: 423px;
    background: radial-gradient(ellipse 620px 420px at 300px 200px, #ffffff 0%, #eef8f8 45%, var(--sky) 100%);
  }
  .board__ground {
    position: absolute;
    left: 0; top: 423px;
    width: 1181px; height: 758px;
    background: var(--olive-board);
  }
  .shapes {
    position: absolute;
    left: 0; top: 0;
    width: 1181px; height: 1181px;
  }
  .suite-list {
    position: absolute;
    left: 88px; top: 462px;
    margin: 0; padding: 0;
    list-style: none;
    font-family: 'Josefin Sans', sans-serif;
    font-weight: 300;
    font-size: 26px;
    line-height: 30px;
    color: var(--paper);
  }
  .wordmark {
    position: absolute;
    font-family: 'Questrial', sans-serif;
    color: var(--brand-green);
    text-align: center;
    white-space: nowrap;
    line-height: 1;
  }
  .wordmark__name { display: block; }
  .wordmark__sub {
    display: block;
    font-size: 0.3em;
    letter-spacing: 0.8em;
    margin-top: 0.6em;
    margin-right: -0.8em;
  }
  .wordmark--hero { left: 184px; top: 190px; font-size: 39px; width: 276px; }
  .wordmark--card-a { left: 707px; top: 182px; font-size: 17px; width: 124px; }
  .wordmark--card-b { left: 926px; top: 254px; font-size: 14px; width: 100px; }
  .wordmark--letterhead { left: 688px; top: 562px; font-size: 14px; width: 102px; }
  .wordmark--envelope { left: 116px; top: 774px; font-size: 8px; width: 57px; }
  .wordmark--business { left: 148px; top: 938px; font-size: 22px; width: 160px; }
</style>
</head>
<body>
<main class="board">
  <div class="board__sky"></div>
  <div class="board__ground"></div>

  <svg class="shapes" viewBox="0 0 1181 1181" aria-hidden="true">
    <g class="card-front">
      <rect x="687" y="128" width="168" height="328" fill="var(--paper)"/>
      <polygon points="733,300 826,350 803,359" fill="var(--lime)"/>
      <polygon points="687,296 803,359 855,336 855,456 687,456" fill="var(--olive-dark)"/>
    </g>
    <g class="card-back">
      <rect x="878" y="128" width="168" height="328" fill="var(--paper)"/>
      <polygon points="878,128 1046,128 1046,221 994,196 878,261" fill="var(--olive-dark)"/>
      <polygon points="878,336 923,312 1046,378 1046,456 878,456" fill="var(--lime)"/>
    </g>
    <g class="envelope">
      <rect x="90" y="596" width="493" height="224" fill="var(--paper)"/>
      <polygon points="90,596 583,596 583,620 336,679 90,620" fill="var(--lime)"/>
    </g>
    <g class="business-card">
      <rect x="90" y="848" width="493" height="224" fill="var(--paper)"/>
      <polygon points="403,848 507,848 412,1010 467,1072 340,1072 438,913" fill="var(--olive-dark)"/>
      <polygon points="507,848 583,848 583,1072 467,1072 412,1010" fill="var(--lime)"/>
    </g>
    <g class="letterhead">
      <rect x="667" y="527" width="422" height="541" fill="var(--paper)"/>
      <polygon points="667,527 1089,527 1089,577 962,528 667,578" fill="var(--lime)"/>
      <polygon points="667,1068 732,1037 1089,1068" fill="var(--olive-dark)"/>
    </g>
  </svg>

  <ul class="suite-list">
    <li>Cards</li>
    <li>Letterhead</li>
    <li>Envelope</li>
  </ul>

  <div class="wordmark wordmark--hero"><span class="wordmark__name">Morning Harbor</span><span class="wordmark__sub">COMMUNITY CHAPEL</span></div>
  <div class="wordmark wordmark--card-a"><span class="wordmark__name">Morning Harbor</span><span class="wordmark__sub">COMMUNITY CHAPEL</span></div>
  <div class="wordmark wordmark--card-b"><span class="wordmark__name">Morning Harbor</span><span class="wordmark__sub">COMMUNITY CHAPEL</span></div>
  <div class="wordmark wordmark--letterhead"><span class="wordmark__name">Morning Harbor</span><span class="wordmark__sub">COMMUNITY CHAPEL</span></div>
  <div class="wordmark wordmark--envelope"><span class="wordmark__name">Morning Harbor</span><span class="wordmark__sub">COMMUNITY CHAPEL</span></div>
  <div class="wordmark wordmark--business"><span class="wordmark__name">Morning Harbor</span><span class="wordmark__sub">COMMUNITY CHAPEL</span></div>
</main>
</body>
</html>
```